An international wholesale business needs letterhead design

Logo file is attached. Please design a letterhead with the following details:

- Company Name and Logo
- Address
- VAT Registration number
- Phone No
- Website address

```html
<!DOCTYPE html>
<html lang="en">
<head>
<meta charset="utf-8">
<title>Korvell Trading Letterhead</title>
<link href="https://fonts.googleapis.com/css2?family=Lato:wght@400;700&family=Satisfy&display=swap" rel="stylesheet">
<style>
  :root {
    --brand-red: #c4202b;
    --brand-grey: #8a8f96;
    --ink: #2b2b2b;
    --paper: #ffffff;
    --backdrop: #e4e4e4;
  }
  * { margin: 0; padding: 0; box-sizing: border-box; }
  html, body { width: 1200px; height: 1200px; overflow: hidden; }
  body {
    background: var(--backdrop);
    font-family: "Lato", Arial, sans-serif;
    color: var(--ink);
  }
  .letterhead {
    position: absolute;
    left: 222px; top: 51px;
    width: 756px; height: 1098px;
    background: var(--paper);
    overflow: hidden;
  }
  .band { position: absolute; left: 0; display: block; }
  .band--top { top: 0; }
  .band--bottom { bottom: 0; }

  .brand {
    position: absolute; left: 46px; top: 92px;
    display: flex; align-items: center; gap: 12px;
  }
  .brand__dot {
    width: 56px; height: 56px; border-radius: 50%;
    background: var(--brand-red);
  }
  .brand__name {
    font-size: 29px; font-weight: 700; letter-spacing: 1px;
    color: var(--brand-red);
  }

  .contact {
    position: absolute; left: 518px; top: 70px;
    padding-left: 11px;
    border-left: 2px solid var(--brand-red);
    font-size: 13.5px; line-height: 18px; color: #222;
  }
  .contact__company { font-weight: 700; color: var(--brand-red); margin-bottom: 5px; }
  .contact__company span { color: var(--brand-grey); }
  .contact__address { margin-bottom: 6px; }
  .contact__row { display: flex; align-items: center; gap: 9px; height: 19px; }
  .contact__row svg { width: 11px; height: 11px; flex: none; }

  .letter {
    position: absolute; left: 42px; top: 274px; width: 672px;
    font-size: 13.6px; line-height: 17.5px;
  }
  .letter__date { margin-bottom: 21px; }
  .letter__recipient { margin-bottom: 18px; }
  .letter__salutation { font-size: 19px; font-weight: 700; margin: 4px 0 16px; }
  .letter__body p { text-align: justify; margin-bottom: 17.5px; }
  .letter__closing { margin-top: 40px; }
  .letter__signature {
    font-family: "Satisfy", cursive;
    font-size: 34px; line-height: 40px; margin-top: 28px; color: #111;
  }

  .vat {
    position: absolute; right: 28px; bottom: 12px;
    font-size: 12.5px; color: #fff;
  }
</style>
</head>
<body>
  <main class="letterhead">
    <svg class="band band--top" width="756" height="52" viewBox="0 0 756 52" aria-hidden="true">
      <polygon points="0,0 756,0 756,28 258,28 244,51 0,51" fill="var(--brand-red)"/>
      <polygon points="268,38 457,38 457,48 262,48" fill="var(--brand-grey)"/>
      <rect x="464" y="38" width="137" height="10" fill="var(--brand-red)"/>
      <rect x="608" y="38" width="148" height="10" fill="var(--brand-grey)"/>
    </svg>

    <div class="brand">
      <div class="brand__dot"></div>
      <div class="brand__name">KORVELL TRADING</div>
    </div>

    <address class="contact" style="font-style:normal">
      <div class="contact__company">KORVELL <span>TRADING</span></div>
      <div class="contact__address">1450 W Harbor Blvd Ste 320<br>Dayton, OH 45402</div>
      <div class="contact__row">
        <svg viewBox="0 0 24 24"><path fill="var(--brand-red)" d="M6.6 10.8a15 15 0 0 0 6.6 6.6l2.2-2.2a1 1 0 0 1 1-.25 11.4 11.4 0 0 0 3.6.57 1 1 0 0 1 1 1V20a1 1 0 0 1-1 1A17 17 0 0 1 3 4a1 1 0 0 1 1-1h3.5a1 1 0 0 1 1 1c0 1.25.2 2.45.57 3.57a1 1 0 0 1-.25 1z"/></svg>
        <span>555-214-7730</span>
      </div>
      <div class="contact__row">
        <svg viewBox="0 0 24 24"><path fill="var(--brand-red)" d="M2 5h20v14H2z"/><path fill="none" stroke="#fff" stroke-width="2" d="M2 6l10 7 10-7"/></svg>
        <span>info@korvellmail.com</span>
      </div>
      <div class="contact__row">
        <svg viewBox="0 0 24 24"><circle cx="12" cy="12" r="10" fill="var(--brand-red)"/><path fill="none" stroke="#fff" stroke-width="1.6" d="M2 12h20M12 2c3 3 3 17 0 20M12 2c-3 3-3 17 0 20"/></svg>
        <span>www.korvelltrading.com</span>
      </div>
    </address>

    <article class="letter">
      <p class="letter__date">January-03-2020</p>
      <p class="letter__recipient">Mr, Alan Pryce<br>President</p>
      <p class="letter__recipient">Vantor Holdings<br>48 Orchard Lane, Suite# 12<br>Millbrook, State, 210045</p>
      <p class="letter__salutation">Dear Mr, Alan</p>
      <div class="letter__body">
        <p>Lorem ipsum dolor sit amet, consectetur adipisicing elit, sed do eiusmod tempor incididunt ut labore et dolore magna aliqua. Ut enim ad minim veniam, quis nostrud exercitation ullamco laboris nisi ut aliquip ex ea commodo consequat. Duis aute irure dolor in reprehenderit in voluptate velit esse cillum dolore eu fugiat nulla pariatur.</p>
        <p>Lorem ipsum dolor sit amet, consectetur adipisicing elit, sed do eiusmod tempor incididunt ut labore et dolore magna aliqua. Ut enim ad minim veniam, quis nostrud exercitation ullamco laboris nisi ut aliquip ex ea commodo consequat. Duis aute irure dolor in reprehenderit in voluptate velit esse cillum dolore eu fugiat nulla pariatur.</p>
        <p>Lorem ipsum dolor sit amet, consectetur adipisicing elit, sed do eiusmod tempor incididunt ut labore et dolore magna aliqua. Ut enim ad minim veniam, quis nostrud exercitation ullamco laboris nisi ut aliquip ex ea commodo consequat.</p>
        <p>Excepteur sint occaecat cupidatat non proident, sunt in culpa qui officia deserunt mollit anim id est laborum. re et dolore magnam aliquam quaerat voluptatem.</p>
      </div>
      <p class="letter__closing">Regards</p>
      <p class="letter__signature">Daniel Hart</p>
    </article>

    <svg class="band band--bottom" width="756" height="52" viewBox="0 0 756 52" aria-hidden="true">
      <rect x="0" y="0" width="139" height="10" fill="var(--brand-grey)"/>
      <rect x="147" y="0" width="135" height="10" fill="var(--brand-red)"/>
      <polygon points="289,0 490,0 484,10 289,10" fill="var(--brand-grey)"/>
      <polygon points="0,17 486,17 500,0 756,0 756,52 0,52" fill="var(--brand-red)"/>
    </svg>
    <p class="vat">VAT Registration number: 412 7781</p>
  </main>
</body>
</html>
```